Private London College Prospectus

A single spread to begin with followed by treatments for a couple of awkward spreads in the brochure. Attached docs include previous few years to show how the design has evolved. We're now looking for a different direction
Outline: Private college in Central London.
Mainly A-levels but also GCSE courses
Consistently at the top of London results table
Operated by the owners
Prospectus is sent to anyone enquiring about the college

Target Market(s)

High net worth families in the Uk and abroad

Industry/Entity Type

College

Requirements
Must have
• Modern fonts
• House colour is purple - PMS 8804
• Teacher quote
• Page quote
Nice to have
• See attachments - the gryphon is part of their logo but not essential
Should not have
• Shouldn't be too fussy or cluttered
• No script fonts (probably) no italics in main text

```html
<!DOCTYPE html>
<html lang="en">
<head>
<meta charset="utf-8">
<title>Kensworth College Prospectus Spread</title>
<link href="https://fonts.googleapis.com/css2?family=Open+Sans:wght@300;400;600;700;800&family=Roboto+Condensed:wght@700&display=swap" rel="stylesheet">
<style>
  :root {
    --purple: #4f3a7a;
    --purple-deep: #3e2c66;
    --ink: #3c3c3c;
    --charcoal: #474747;
    --body: #2a2a2a;
    --page: #ffffff;
    --backdrop: #ececec;
    --stripe-grey: #5a5a5a;
  }
  * { box-sizing: border-box; margin: 0; padding: 0; }
  html, body { width: 1200px; height: 1200px; overflow: hidden; }
  body { background: var(--backdrop); font-family: "Open Sans", Arial, sans-serif; position: relative; }

  .spread { position: absolute; left: 10px; top: 176px; width: 1180px; height: 848px; background: var(--page); }

  /* left page */
  .title { position: absolute; left: 48px; top: 40px; line-height: 1; }
  .title-light { display: block; font-weight: 300; font-size: 57px; color: var(--purple); letter-spacing: 0.5px; }
  .title-bold { display: block; font-weight: 700; font-size: 58px; color: var(--ink); letter-spacing: 0.5px; }

  .photo { position: absolute; }
  .hero-photo { left: 3px; top: 175px; width: 592px; height: 370px;
    background: linear-gradient(160deg, #d9d6cf 0%, #5b5a55 35%, #2a2a2c 55%, #7b8d5a 85%, #c9b04a 100%); }

  .banner { position: absolute; left: 3px; top: 550px; width: 530px; height: 56px; }
  .banner-label { position: absolute; left: 55px; top: 557px; font-weight: 800; font-size: 15.5px; color: #fff; letter-spacing: 0.4px; }

  .framed { position: absolute; width: 236px; height: 159px; border: 3px solid var(--purple); background: #fff; padding: 5px; }
  .framed .fill { width: 100%; height: 100%; }
  .frame-class { left: 52px; top: 633px; }
  .frame-class .fill { background: linear-gradient(135deg, #efe2cf 0%, #b9a58c 50%, #6e6358 100%); }
  .frame-students { left: 326px; top: 633px; }
  .frame-students .fill { background: linear-gradient(135deg, #e6e3df 0%, #8c8680 45%, #4a3a36 100%); }

  .footer-bar { position: absolute; left: 3px; top: 820px; width: 592px; height: 25px; background: var(--charcoal); }

  /* spine */
  .spine { position: absolute; left: 595px; top: 0; width: 20px; height: 820px; background: var(--purple); }

  /* right page */
  .lab-photo { left: 949px; top: 0; width: 173px; height: 211px;
    background: linear-gradient(160deg, #6a6a6a 0%, #d8d8d8 40%, #f2f2f2 70%, #9a9a9a 100%); }

  .copy { position: absolute; left: 644px; top: 214px; width: 480px; }
  .copy h2 { font-weight: 400; font-size: 14.5px; color: var(--purple); margin-bottom: 6px; }
  .copy p { font-size: 9.3px; line-height: 12px; color: var(--body); margin-bottom: 12px; letter-spacing: -0.1px; }
  .copy p.section-end { margin-bottom: 20px; }

  .teacher-band { position: absolute; left: 615px; top: 620px; width: 565px; height: 200px; }
  .teacher-photo { left: 600px; top: 628px; width: 192px; height: 192px;
    background: radial-gradient(ellipse at 50% 35%, #b08a70 0%, #8a6a58 25%, #e9e9e9 55%, #ffffff 100%); }
  .teacher-name { position: absolute; left: 801px; top: 730px; font-family: "Roboto Condensed", Arial, sans-serif; font-weight: 700; font-size: 17.5px; line-height: 1; color: #fff; letter-spacing: 0.3px; }
  .teacher-role { position: absolute; left: 801px; top: 750px; font-weight: 600; font-size: 13px; line-height: 1.2; color: #fff; }
  .teacher-quote { position: absolute; left: 801px; top: 774px; width: 205px; font-size: 8.3px; line-height: 11px; color: #fff; }
  .frame-seminar { position: absolute; left: 992px; top: 637px; width: 176px; height: 122px; border: 3px solid #fff; background: #fff; padding: 3px; }
  .frame-seminar .fill { width: 100%; height: 100%; background: linear-gradient(135deg, #e9e0d0 0%, #c7a878 50%, #8a7a6a 100%); }
</style>
</head>
<body>
  <main class="spread">
    <!-- left page -->
    <h1 class="title">
      <span class="title-light">PRIVATE COLLEGE IN</span>
      <span class="title-bold">CENTRAL LONDON</span>
    </h1>

    <div class="photo hero-photo" role="img" aria-label="Group of five students standing at the college's black front door between potted trees and daffodils"></div>

    <svg class="banner" viewBox="0 0 530 56" width="530" height="56">
      <polygon points="0,0 510,0 522,36 0,36" fill="#4f3a7a"/>
      <polygon points="496,38 522,38 496,56" fill="#3e2c66"/>
    </svg>
    <div class="banner-label">BENEFITS OF THE MANAGED ACCOUNT OF FUNDS ?</div>

    <div class="framed frame-class"><div class="fill" role="img" aria-label="Students seated around tables in a bright classroom with a wall map"></div></div>
    <div class="framed frame-students"><div class="fill" role="img" aria-label="Two smiling students working at a desk"></div></div>

    <div class="footer-bar"></div>

    <div class="spine"></div>

    <!-- right page -->
    <div class="photo lab-photo" role="img" aria-label="Black and white photo of students in lab coats using microscopes"></div>

    <section class="copy">
      <h2>The Kensworth Ethos</h2>
      <p class="section-end">Based in the heart of Mayfair in central London, Kensworth is a top performing independent sixth-form college, offering a broad A-level and GCSE curriculum for students from public, state and private school backgrounds.</p>

      <h2>Why Choose Kensworth?</h2>
      <p>The majority of students who come to Kensworth do so because of our reputation for excellent A-level and GCSE results. This is true of students both on our full two-year programme, as well as those on the one-year intensive programme. Most students will progress on to a top 20 UK university.</p>
      <p class="section-end">Students are taught very much by traditional methods, in small groups, concentrating on the skills needed to pass examinations and to be successful at university. All teachers at Kensworth are subject specialists and most have experience as examiners. They are particularly successful with young people: they are able to motivate and communicate with them in ways which they understand. Barriers are quickly broken down, enhancing the learning process.</p>

      <h2>How Do We Get The Best Out Of Our Students?</h2>
      <p>Students benefit from individually tailored attention outside of classes – a key element of our successful A-level and GCSE programmes, and at Kensworth each student has a Curriculum Manager and a Personal Tutor, who provide advice on study skills, subject choices and careers, and who also monitor progress in regular meetings with students.</p>
      <p>We expect full commitment from our students and as such we have strict rules on attendance and timely submission of assignments. Parents are able to monitor progress through monthly reports, easily accessible using our online reporting system. Parents' Evenings are held during the Autumn and Spring terms.</p>
      <p>We encourage our students every step of the way and we help them to build confidence through examination success. We see the learning process as a successful partnership between students, tutors and parents.</p>
    </section>

    <svg class="teacher-band" viewBox="0 0 565 200" width="565" height="200">
      <polygon points="0,128 375,50 375,58 0,136" fill="#5a5a5a"/>
      <polygon points="0,146 375,66 565,10 565,200 0,200" fill="#4f3a7a"/>
    </svg>
    <div class="photo teacher-photo" role="img" aria-label="Portrait of the Head of Economics in a white shirt"></div>
    <div class="teacher-name">RAJAN MEHTA</div>
    <div class="teacher-role">Head of Economics</div>
    <p class="teacher-quote">We teach students how to develop their powers of analysis and independence of thought - crucial to success at university and beyond.</p>
    <div class="frame-seminar"><div class="fill" role="img" aria-label="Seminar room with students around a horseshoe table and a teacher standing"></div></div>
  </main>
</body>
</html>
```